Business Design for Printed Shipping Tape

We need a company logo design to be printed on packaging natural color WAT tape for shipping boxes. www.brightmeadowkelp.com
The tape is 3" wide. Repeat pattern every 10 inches.
Would like our website vertical at one end side and "The Future of Nutrition" on the opposite end.

Industry/Entity Type

Health, Nutrition

Font styles to use
Sans Serif

Requirements
Must have
• Company Logo (attached) website and text "The Future of Nutrition"
Nice to have
• Tape is Natural Color.

```html
<!DOCTYPE html>
<html lang="en">
<head>
<meta charset="utf-8">
<title>Bright Meadow Kelp – Shipping Tape</title>
<link href="https://fonts.googleapis.com/css2?family=Poppins:ital,wght@0,400;0,700;1,400;1,600;1,700&display=swap" rel="stylesheet">
<style>
  :root {
    --backdrop: #8e8e8e;
    --tape-white: #ffffff;
    --kelp-green: #2d431b;
    --ink: #333333;
    --accent: #2f8f7e;
  }
  html, body {
    margin: 0;
    width: 900px;
    height: 1200px;
    overflow: hidden;
    background: var(--backdrop);
    font-family: "Poppins", sans-serif;
  }
  .tape-strip {
    position: absolute;
    left: 40px;
    top: 477px;
    width: 820px;
    height: 246px;
    background: var(--tape-white);
    box-shadow: 0 6px 18px rgba(0,0,0,0.25);
  }
  .slogan-band {
    position: absolute;
    inset: 0;
    width: 100%;
    height: 100%;
  }
  .brand-mark {
    position: absolute;
    left: 20px;
    width: 320px;
    top: 44px;
    text-align: center;
  }
  .brand-dot {
    display: block;
    width: 38px;
    height: 38px;
    margin: 0 auto 10px;
    border-radius: 50%;
    background: var(--accent);
  }
  .brand-name {
    margin: 0;
    font-weight: 700;
    font-size: 34px;
    line-height: 1.05;
    letter-spacing: -0.5px;
    color: var(--ink);
    text-transform: uppercase;
  }
  .site-url {
    position: absolute;
    top: 123px;
    font-size: 12px;
    color: var(--ink);
    white-space: nowrap;
    transform: translate(-50%, -50%) rotate(-90deg);
  }
  .site-url--left { left: 365px; }
  .site-url--right { left: 780px; }
  .slogan {
    position: absolute;
    inset: 0;
    color: var(--tape-white);
    font-style: italic;
  }
  .slogan span {
    position: absolute;
    line-height: 1;
    white-space: nowrap;
  }
  .slogan-the { left: 482px; top: 44px; font-size: 35px; font-weight: 400; }
  .slogan-future { left: 450px; top: 78px; font-size: 50px; font-weight: 700; letter-spacing: -1px; }
  .slogan-of { font-size: 33px; font-weight: 400; position: static !important; margin-left: 4px; letter-spacing: 0; }
  .slogan-nutrition { left: 471px; top: 138px; font-size: 47px; font-weight: 700; }
</style>
</head>
<body>
  <div class="tape-strip">
    <svg class="slogan-band" viewBox="0 0 1133 340" preserveAspectRatio="none" aria-hidden="true">
      <polygon points="526,0 975,0 1058,340 609,340" fill="var(--kelp-green)"/>
    </svg>

    <div class="brand-mark">
      <span class="brand-dot"></span>
      <p class="brand-name">Bright Meadow<br>Kelp</p>
    </div>

    <span class="site-url site-url--left">BrightMeadowKelp.com</span>

    <div class="slogan">
      <span class="slogan-the">the</span>
      <span class="slogan-future">future<span class="slogan-of">of</span></span>
      <span class="slogan-nutrition">Nutrition</span>
    </div>

    <span class="site-url site-url--right">BrightMeadowKelp.com</span>
  </div>
</body>
</html>
```